Wordpress Website design partner needed for an Arabic Language Institute for English Speakers

We are an online Arabic Language institute, targeting English Speakers around the world and we provide online courses and private group and one on one classes
We are looking for a total of 5 pages designed.
The Design should be mobile-first, and then provide PC for any differences.
I am looking for a consistent design with a lot of white space and in line with our Logo colours.
Images used should be around the theme of Arabic Language/Islamic in Nature, so please do not use any illustrations or images of animals or human beings except for silhouettes or images without faces visible, such as someone facing other way or below torso or hands etc.
The website will eventually be prepared for Wordpress using Divi.
I will provide a very structured outline of what elements and modules each page should have. Therefore I am looking for someone that has an eye for detail and is precise in executing requirements.
I decided to post on this site because I am looking for a long-term partner that can take care of any of our design needs as they come up.
More details to follow
I will do abit more research tomorrow to suggest sample sites
Updates
Gathering more feedback
Target Market(s)
English speakers that want to learn Arabic for Religous purposes such as understanding the Quran
Industry/Entity Type
Education
Colors
Designer to choose colors to be used in the design.
Requirements
Must have
- Mobile First, and design for PC for changes
- Consistency
- Plenty of White Space
- Colour Palette based on Logo
- Colour and Transparent/White Header for when scrolling
- Big Call to Action buttons with contrasting colors
- A consistent footer for all pages with
- -Social Media Icons
- -Contact us
- -Sitemap
- -Copyright
- -Logo
- Anything with a hashtag (#) beforehand in the Doc file means it should be a module like the modules used in Divi Theme, Please check the following website for an explanation of what each module consists of and some examples of it in use. https://www.plumeworkgallery.com/block-parts-guide/
Nice to have
- Parallax Effect
Should not have
- illustrations or images of animals or human beings except for silhouettes or images without faces visible, such as someone facing other way or below torso or hands etc.

```html
<!DOCTYPE html>
<html lang="en">
<head>
<meta charset="utf-8">
<title>Al-Mabda Arabic Academy</title>
<link rel="stylesheet" href="https://fonts.googleapis.com/css2?family=Fira+Sans:wght@300;400;500;600;700&display=swap">
<style>
:root{
  --teal:#2a96a8;
  --blue:#1b57a3;
  --blue-deep:#12479b;
  --ink:#1c1c1c;
  --soft:#f4f0f0;
  --dark:#202020;
  --footer:#262626;
  --muted:#555;
  --white:#fff;
}
*{box-sizing:border-box;margin:0;padding:0}
html,body{width:1200px;height:3990px;overflow:hidden}
body{font-family:"Fira Sans",sans-serif;color:var(--ink);background:var(--white);position:relative}
a{text-decoration:none}
section,header,footer{position:absolute;left:0;width:1200px}
.btn{display:inline-block;background:var(--teal);color:var(--white);font-weight:500;text-transform:uppercase;letter-spacing:.3px;text-align:center;position:absolute;text-decoration:none}
.section-title{position:absolute;left:0;width:1200px;text-align:center;font-size:28px;font-weight:500;letter-spacing:.5px}
.section-title::after{content:"";display:block;width:52px;height:4px;background:var(--teal);margin:16px auto 0}

/* header */
.site-header{top:0;height:88px;background:var(--white)}
.brand{position:absolute;left:131px;top:0;width:99px;height:137px;background:var(--white);box-shadow:0 2px 6px rgba(0,0,0,.15);display:flex;flex-direction:column;align-items:center;justify-content:center;gap:10px;z-index:3}
.brand-mark{width:46px;height:46px;background:var(--teal)}
.brand-name{font-size:13px;font-weight:600;letter-spacing:1.5px;color:var(--ink)}
.main-nav{position:absolute;right:130px;top:34px;display:flex;gap:40px;font-size:16px;font-weight:500}
.main-nav a{color:var(--ink)}
.main-nav a.active{color:var(--teal);text-decoration:underline}

/* intro band */
.intro-band{top:88px;height:245px;background:linear-gradient(100deg,#1b5aa6,#1a4f98 60%,#1d5ba6)}
.intro-text{position:absolute;left:255px;width:690px;top:42px;text-align:center;color:var(--white);font-size:21px;line-height:29px;font-weight:500}
.intro-band .btn{left:467px;top:152px;width:266px;height:56px;line-height:56px;font-size:18px}
.play{display:inline-block;width:22px;height:22px;border-radius:50%;background:var(--white);vertical-align:-5px;margin-right:10px;position:relative}
.play::after{content:"";position:absolute;left:8px;top:6px;border-left:9px solid var(--teal);border-top:5px solid transparent;border-bottom:5px solid transparent}

/* slider */
.hero-slider{top:333px;height:504px}
.hero-photo{position:absolute;inset:0;background:linear-gradient(110deg,#2a2320 0%,#4a3527 40%,#7a5a3d 65%,#3a2a20 100%)}
.hero-copy{position:absolute;left:131px;top:166px;color:var(--white)}
.hero-copy .kicker{font-size:32px;font-weight:600;letter-spacing:1px}
.hero-copy h1{font-size:66px;font-weight:700;letter-spacing:1px;line-height:1.1}
.hero-slider .btn{left:132px;top:309px;width:140px;height:51px;line-height:51px;font-size:18px}
.dots{position:absolute;top:460px;left:550px;display:flex;gap:17px}
.dots span{width:9px;height:9px;border-radius:50%;background:var(--white)}
.dots span.on{background:var(--teal)}

/* benefits */
.benefits{top:837px;height:493px;background:var(--soft)}
.benefits .section-title{top:48px}
.benefit{position:absolute;top:155px;width:260px;text-align:center}
.benefit svg{display:block;margin:0 auto;width:100px;height:100px}
.benefit h3{font-size:18px;font-weight:500;margin-top:50px}
.benefit p{font-size:14px;line-height:19px;margin-top:14px;color:#333;font-weight:400}

/* testimonials */
.testimonials{top:1330px;height:606px}
.testimonials .section-title{top:54px}
.quote{position:absolute;left:131px;width:937px;height:183px;background:var(--soft)}
.quote.highlight{background:var(--teal);color:var(--white)}
.avatar{position:absolute;left:40px;top:36px;width:92px;height:92px;border-radius:50%;background:linear-gradient(180deg,#8c8fa8,#3a2d25)}
.quote.highlight .avatar{background:linear-gradient(180deg,#3a3a48,#1a1a22)}
.quote p{position:absolute;left:170px;top:31px;width:700px;font-size:15px;line-height:21px}
.quote .who{position:absolute;left:170px;top:112px;font-size:12px;line-height:16px}
.quote .who b{font-weight:600}

/* strategy */
.strategy{top:1936px;height:450px;background:var(--soft)}
.strategy-photo{position:absolute;left:0;top:0;width:612px;height:450px;background:linear-gradient(120deg,#cfc4bb,#b79a86 50%,#9fb6c2)}
.strategy h2{position:absolute;left:680px;top:56px;width:350px;font-size:27px;line-height:36px;font-weight:500}
.strategy p{position:absolute;left:680px;top:209px;width:370px;font-size:15px;line-height:21.5px;color:#333}
.strategy .btn{left:682px;top:331px;width:191px;height:51px;line-height:51px;font-size:17px}

/* countdown */
.countdown{top:2386px;height:262px;background:var(--dark);color:var(--white);text-align:center}
.countdown h2{position:absolute;top:50px;width:1200px;font-size:27px;font-weight:400}
.timer{position:absolute;top:112px;left:0;width:1200px}
.unit{position:absolute;width:120px;text-align:center;font-weight:300}
.unit b{display:block;font-size:56px;font-weight:300;line-height:64px}
.unit span{font-size:15px;color:#bbb}
.sep{position:absolute;font-size:46px;font-weight:300;top:6px}

/* features */
.features{top:2648px;height:617px}
.features .section-title{top:64px}
.acc{position:absolute;left:165px;width:871px;border:2px solid #d4d0d0;background:var(--soft);font-size:15px}
.acc .head{height:42px;line-height:42px;padding-left:18px;position:relative}
.acc .head::after{content:"";position:absolute;right:22px;top:13px;width:9px;height:9px;border-right:2px solid #555;border-bottom:2px solid #555;transform:rotate(45deg)}
.acc.open .head{font-weight:600;height:52px;line-height:52px}
.acc.open .head::after{transform:rotate(-135deg);top:22px}
.acc .body{padding:2px 36px 0 30px;font-size:14px;line-height:19px;color:#333}

/* contact */
.contact{top:3265px;height:351px;background:var(--blue-deep);color:var(--white)}
.contact h2{position:absolute;left:130px;top:54px;font-size:28px;font-weight:600}
.contact p{position:absolute;left:130px;top:110px;width:490px;font-size:15px;line-height:21.5px}
.field{position:absolute;left:696px;width:372px;height:48px;background:var(--white);color:#444;font-size:15px;line-height:48px;padding-left:17px}
.contact .btn{left:696px;top:247px;width:372px;height:55px;line-height:55px;font-size:20px;font-weight:600}

/* footer */
.site-footer{top:3616px;height:374px;background:var(--footer);color:var(--white)}
.foot-col-title{position:absolute;font-size:14px;font-weight:500;top:56px}
.foot-item{position:absolute;display:flex;align-items:center;gap:14px;font-size:13px;line-height:16px}
.dot-ico{width:33px;height:33px;border-radius:50%;background:var(--teal);display:flex;align-items:center;justify-content:center;flex:none}
.foot-item .lbl{font-size:11.5px}
.foot-item b{font-weight:500;font-size:14px}
.foot-brand{position:absolute;left:429px;top:56px;width:342px;height:166px;border-left:1px solid #999;border-right:1px solid #999;border-bottom:1px solid #999}
.foot-brand .cover{position:absolute;left:105px;bottom:-2px;width:132px;height:40px;background:var(--footer)}
.foot-brand .mark{position:absolute;left:146px;top:10px;width:50px;height:50px;background:var(--white)}
.foot-brand .name{position:absolute;left:0;width:340px;top:118px;text-align:center;font-size:19px;font-weight:600;letter-spacing:3px}
.foot-nav{position:absolute;left:426px;top:247px;display:flex;gap:18px;font-size:14px;font-weight:500}
.foot-rule{position:absolute;left:131px;top:310px;width:937px;height:1px;background:#666}
.copyright{position:absolute;top:340px;width:1200px;text-align:center;font-size:11px;color:#ccc}
</style>
</head>
<body>

<header class="site-header">
  <div class="brand"><div class="brand-mark"></div><div class="brand-name">AL-MABDA</div></div>
  <nav class="main-nav">
    <a class="active" href="#">HOME</a><a href="#">ABOUT US</a><a href="#">OUR COURSES</a><a href="#">CONTACT US</a>
  </nav>
</header>

<section class="intro-band">
  <p class="intro-text">The Arabic Language Academy which helps understand Allah's words and the Noble Prophets teachings directly in the most Effective, Efficient and Effortless way. Never rely on translations again!</p>
  <a class="btn" href="#"><span class="play"></span>Start Learning Now</a>
</section>

<section class="hero-slider">
  <div class="hero-photo" role="img" aria-label="Open Quran resting on a carved wooden stand over a patterned rug"></div>
  <div class="hero-copy"><div class="kicker">WELCOME TO</div><h1>AL - MABDA</h1></div>
  <a class="btn" href="#">Read More</a>
  <div class="dots"><span></span><span></span><span class="on"></span><span></span><span></span></div>
</section>

<section class="benefits">
  <h2 class="section-title">BENEFITS</h2>
  <div class="benefit" style="left:125px">
    <svg viewBox="0 0 100 100" fill="none" stroke="#2a96a8" stroke-width="4" stroke-linecap="round">
      <path d="M38 62c0-8-10-12-10-26a22 22 0 0 1 44 0c0 14-10 18-10 26z"/>
      <path d="M40 70h20M42 78h16M46 86h8"/>
      <path d="M50 2v8M20 12l6 6M80 12l-6 6M6 38h10M84 38h10M16 64l6-5M84 64l-6-5"/>
    </svg>
    <h3>EFFICIENT</h3>
    <p>Lorem ipsum dolor sit amet conse ctetur adipiscing elit sed do eiusmod tempor incididunt ut labore et dolore magna aliqua. Ut enim ad minim veniam quis nos trud .</p>
  </div>
  <div class="benefit" style="left:470px">
    <svg viewBox="0 0 100 100" fill="none" stroke="#2a96a8" stroke-width="4" stroke-linejoin="round">
      <path d="M4 34l16-16 14 14-16 16zM96 34L80 18 66 32l16 16z"/>
      <path d="M34 32l14-8 10 4 8 4M66 32L52 46c-4 4-10 0-6-4l8-8"/>
      <path d="M18 48l26 26c4 4 8 2 10 0l26-26"/>
      <path d="M30 60l8 8M38 54l10 10M46 50l10 10"/>
    </svg>
    <h3>EFFECTIVE</h3>
    <p>Lorem ipsum dolor sit amet conse ctetur adipiscing elit sed do eiusmod tempor incididunt ut labore et dolore magna aliqua. Ut enim ad minim veniam quis nos trud .</p>
  </div>
  <div class="benefit" style="left:817px">
    <svg viewBox="0 0 100 100" fill="none" stroke="#2a96a8" stroke-width="4" stroke-linejoin="round" stroke-linecap="round">
      <circle cx="60" cy="30" r="16"/><circle cx="60" cy="30" r="22" stroke-dasharray="6 5"/>
      <path d="M52 30l6 6 10-12"/>
      <path d="M6 66h14v22H6zM20 70h18c6 0 8 6 14 6h10M20 84h30l36-16c4-2 2-8-2-8l-22 6"/>
    </svg>
    <h3>EFFORTLESS</h3>
    <p>Lorem ipsum dolor sit amet conse ctetur adipiscing elit sed do eiusmod tempor incididunt ut labore et dolore magna aliqua. Ut enim ad minim veniam quis nos trud .</p>
  </div>
</section>

<section class="testimonials">
  <h2 class="section-title">TESTIMONIALS</h2>
  <article class="quote" style="top:150px">
    <div class="avatar" role="img" aria-label="Mosque dome silhouetted at sunset with a crescent"></div>
    <p>Lorem ipsum dolor sit amet, consectetur adipiscing elit, sed do eiusmod tempor incididunt ut labore et dolore magna aliqua. Ut enim ad minim veniam, quis nostrud exercitation ullamco laboris nisi ut aliquip ex ea commodo consequat. Duis aute irure dolor in reprehende</p>
    <div class="who"><b>DANIEL</b><br>General Manager</div>
  </article>
  <article class="quote highlight" style="top:359px">
    <div class="avatar" role="img" aria-label="Open Quran on a stand in low light"></div>
    <p>Lorem ipsum dolor sit amet, consectetur adipiscing elit, sed do eiusmod tempor incididunt ut labore et dolore magna aliqua. Ut enim ad minim veniam, quis nostrud exercitation ullamco laboris nisi ut aliquip ex ea commodo consequat. Duis aute irure dolor in reprehende</p>
    <div class="who"><b>DANIEL</b><br>General Manager</div>
  </article>
</section>

<section class="strategy">
  <div class="strategy-photo" role="img" aria-label="Cupped hands raised in prayer holding prayer beads"></div>
  <h2>7 LEARNING STRATEGIES THAT WILL BOOST YOUR ARABIC LEARNING</h2>
  <p>Lorem ipsum dolor sit amet, consectetur adipiscing elit, sed do eiusmod tempor incididunt ut labore et dolore magna aliqua. Ut enim ad minim veniam, quis nostrud exercitation ullamco laboris nisi ut.</p>
  <a class="btn" href="#">Book Your Spot</a>
</section>

<section class="countdown">
  <h2>Launching in</h2>
  <div class="timer">
    <div class="unit" style="left:270px"><b>156</b><span>Days</span></div>
    <div class="sep" style="left:415px">:</div>
    <div class="unit" style="left:455px"><b>10</b><span>Hours</span></div>
    <div class="sep" style="left:595px">:</div>
    <div class="unit" style="left:639px"><b>31</b><span>Minutes</span></div>
    <div class="sep" style="left:782px">:</div>
    <div class="unit" style="left:825px"><b>55</b><span>Seconds</span></div>
  </div>
</section>

<section class="features">
  <h2 class="section-title">FEATURES</h2>
  <div class="acc" style="top:145px"><div class="head">24/7 Access</div></div>
  <div class="acc" style="top:204px"><div class="head">Learn at your own Pace</div></div>
  <div class="acc" style="top:264px"><div class="head">Certificate</div></div>
  <div class="acc" style="top:324px"><div class="head">Free Study Material</div></div>
  <div class="acc open" style="top:384px;height:190px">
    <div class="head">Qualified Teachers</div>
    <div class="body">Lorem ipsum dolor sit amet, consectetur adipiscing elit, sed do eiusmod tempor incididunt ut labore et dolore magna aliqua. Ut enim ad minim veniam, quis nostrud exercitation ullamco laboris nisi ut aliquip ex ea commodo consequat. Duis aute irure dolor in reprehenderit in voluptate velit esse cillum dolore eu fugiat nulla pariatur. Excepteur sint occaecat cupidatat non proident, sunt in culpa qui officia deserunt mollit anim id est laborum. Nemo enim ipsam voluptatem quia voluptas sit aspernatur aut odit aut fugit, sed quia consequuntur magni dolores</div>
  </div>
</section>

<section class="contact">
  <h2>CONTACT US</h2>
  <p>At vero eos et accusamus et iusto odio dignissimos ducimus qui blanditiis praesentium voluptatum deleniti atque corrupti quos dolores et quas molestias excepturi sint occaecati cupiditate non provident, similique sunt in culpa qui officia deserunt mollitia animi, id est laborum et dolorum fuga. Et harum quidem rerum facilis est et expedita distinctio. Nam libero tempore, cum soluta nobis est eligendi optio cumque nihil impedit quo minus id quod maxime placeat facere possimus, omnis voluptas assumend.</p>
  <div class="field" style="top:62px">First Name</div>
  <div class="field" style="top:120px">Last Name</div>
  <div class="field" style="top:179px">E mail</div>
  <a class="btn" href="#">Join Today</a>
</section>

<footer class="site-footer">
  <div class="foot-col-title" style="left:136px">CONTACT US</div>
  <div class="foot-item" style="left:133px;top:101px">
    <span class="dot-ico"><svg width="16" height="16" viewBox="0 0 24 24" fill="#fff"><path d="M6.6 10.8a15 15 0 0 0 6.6 6.6l2.2-2.2c.3-.3.7-.4 1-.2 1.1.4 2.3.6 3.6.6.6 0 1 .4 1 1V20c0 .6-.4 1-1 1A17 17 0 0 1 3 4c0-.6.4-1 1-1h3.5c.6 0 1 .4 1 1 0 1.3.2 2.5.6 3.6.1.3 0 .7-.2 1z"/></svg></span>
    <div><span class="lbl">CALL US</span><br><b>555.010.2030</b></div>
  </div>
  <div class="foot-item" style="left:133px;top:179px">
    <span class="dot-ico"><svg width="16" height="12" viewBox="0 0 16 12" fill="#fff"><path d="M0 0h16v1.5L8 6.5 0 1.5zM0 3.3l8 5 8-5V12H0z"/></svg></span>
    <div><span class="lbl">E MAIL US</span><br><b>info@almabda-academy.com</b></div>
  </div>

  <div class="foot-brand">
    <div class="cover"></div>
    <div class="mark"></div>
    <div class="name">AL-MABDA</div>
  </div>
  <nav class="foot-nav"><span>HOME</span><span>ABOUT US</span><span>OUR COURSES</span><span>CONTACT US</span></nav>

  <div class="foot-col-title" style="left:894px">FOLLOW US</div>
  <div class="foot-item" style="left:892px;top:114px"><span class="dot-ico" style="width:29px;height:29px"></span><div>Like us on<br>KINDRA</div></div>
  <div class="foot-item" style="left:892px;top:174px"><span class="dot-ico" style="width:29px;height:29px"></span><div>Follow us on<br>PEEPLINE</div></div>
  <div class="foot-item" style="left:892px;top:235px"><span class="dot-ico" style="width:29px;height:29px"></span><div>Follow us on<br>PROFILIO</div></div>

  <div class="foot-rule"></div>
  <div class="copyright">Copyright © 2020 All Rights Reserved</div>
</footer>

</body>
</html>
```